Bright Horizon Rewards marketing promotion flier!

Currently in the process of revitalizing our marketing fliers for the year 2024. Our leadership team has expressed their keen interest in embracing a rejuvenated appearance for the upcoming year. In order to achieve this, we are seeking an alternative flyer layout that effectively incorporates the same information. To provide an example, the CEO has created a mock-up of the program, along with last year's flier, solely for illustrative purposes. It is important to emphasize that we are aiming for a completely new and refreshed look.

Target Market(s)

Customers

Industry/Entity Type

roofing

Colors
0054AA
0677BA
7BADD7
CADEEF
E8F1F8
0094D4
00A9DD
6FCCEA
C7EBF8
E9F6FB

Requirements
Must have
• The information from 2023 flier
Should not have
• the same look as least year

```html
<!DOCTYPE html>
<html lang="en">
<head>
<meta charset="utf-8">
<title>Bright Horizon Rewards – 2024 Promotion</title>
<link href="https://fonts.googleapis.com/css2?family=Bebas+Neue&family=Poppins:wght@400;500;600;700;800;900&family=Stardos+Stencil:wght@700&display=swap" rel="stylesheet">
<style>
  :root {
    --paper: #fbeee2;
    --navy: #1b2f57;
    --royal: #0b2590;
    --royal-light: #8a90c2;
    --ink-blue: #1f2f86;
    --offer-blue: #0b4f9c;
    --red: #c8102e;
    --text: #2a2a2a;
    --white: #ffffff;
  }
  * { margin: 0; padding: 0; box-sizing: border-box; }
  html, body { width: 952px; height: 1200px; overflow: hidden; background: var(--paper); }
  .flier {
    position: relative;
    width: 952px;
    height: 1200px;
    background: var(--paper);
    font-family: "Poppins", sans-serif;
    color: var(--text);
  }
  .brand-mark {
    position: absolute;
    top: 84px;
    width: 196px;
    text-align: center;
    font-family: "Poppins", sans-serif;
    font-weight: 700;
    font-size: 18px;
    color: var(--royal);
    letter-spacing: 0.5px;
  }
  .brand-mark--left { left: 48px; }
  .brand-mark--right { right: 48px; }
  .year {
    position: absolute;
    top: 30px;
    left: 0;
    width: 100%;
    text-align: center;
    font-family: "Poppins", sans-serif;
    font-weight: 900;
    font-size: 178px;
    line-height: 1;
    letter-spacing: -10px;
    background: linear-gradient(180deg, var(--royal-light) 0%, var(--royal) 70%);
    -webkit-background-clip: text;
    background-clip: text;
    color: transparent;
  }
  .headline {
    position: absolute;
    left: 0;
    width: 100%;
    text-align: center;
    font-family: "Stardos Stencil", serif;
    font-weight: 700;
    line-height: 1;
  }
  .headline--top { top: 198px; font-size: 82px; color: var(--red); letter-spacing: 1px; }
  .headline--bottom { top: 270px; font-size: 92px; color: var(--ink-blue); letter-spacing: 1px; }
  .hero-art {
    position: absolute;
    top: 367px;
    left: 97px;
    width: 745px;
    height: 462px;
    background:
      linear-gradient(180deg, rgba(27,47,87,0) 45%, rgba(27,47,87,0.95) 100%),
      linear-gradient(90deg, #6d93cf 0%, #2f5fb8 42%, #d83a4c 55%, #f2c8cc 80%, #e04a5a 100%);
    border-radius: 4px;
  }
  .offer-line {
    position: absolute;
    top: 836px;
    left: 0;
    width: 100%;
    text-align: center;
    font-family: "Bebas Neue", sans-serif;
    font-size: 66px;
    line-height: 1;
    color: var(--offer-blue);
  }
  .offer-line .accent { color: var(--red); }
  .discount-band {
    position: absolute;
    top: 905px;
    left: 115px;
    width: 716px;
    height: 70px;
    display: flex;
    background: var(--navy);
    border-radius: 10px;
    border: 2px solid var(--navy);
    overflow: hidden;
  }
  .discount-amount {
    width: 328px;
    display: flex;
    align-items: center;
    justify-content: center;
    color: var(--white);
    gap: 12px;
  }
  .discount-amount .value { font-weight: 700; font-size: 56px; line-height: 1; }
  .discount-amount .off { font-weight: 700; font-size: 28px; letter-spacing: 8px; }
  .discount-audience {
    flex: 1;
    background: var(--white);
    border-radius: 9px;
    display: flex;
    align-items: center;
    justify-content: center;
    font-family: "Bebas Neue", sans-serif;
    font-size: 34px;
    color: var(--navy);
  }
  .credit-line {
    position: absolute;
    top: 990px;
    left: 0;
    width: 100%;
    text-align: center;
    font-weight: 500;
    font-size: 22px;
    line-height: 1.2;
    color: var(--text);
  }
  .credit-line .accent { color: var(--red); font-weight: 600; }
  .credit-note {
    position: absolute;
    top: 1020px;
    left: 0;
    width: 100%;
    text-align: center;
    font-size: 18px;
    color: var(--text);
  }
  .order-terms {
    position: absolute;
    top: 1065px;
    left: 71px;
    width: 829px;
    height: 27px;
    background: var(--navy);
    border-radius: 5px;
    color: var(--white);
    font-weight: 600;
    font-size: 16px;
    letter-spacing: 1px;
    text-align: center;
    line-height: 27px;
  }
  .fine-print {
    position: absolute;
    top: 1100px;
    left: 96px;
    width: 794px;
    text-align: center;
    font-size: 8.4px;
    line-height: 1.3;
    color: var(--text);
  }
  .social {
    position: absolute;
    top: 1146px;
    left: 0;
    width: 100%;
    text-align: center;
    font-size: 12px;
    font-weight: 500;
    color: var(--text);
  }
</style>
</head>
<body>
<main class="flier">
  <div class="brand-mark brand-mark--left">HARBORLINE SUPPLY</div>
  <div class="brand-mark brand-mark--right">HARBORLINE SUPPLY</div>

  <div class="year">2024</div>
  <h1 class="headline headline--top">BRIGHT</h1>
  <h2 class="headline headline--bottom">HORIZON REWARDS</h2>

  <div class="hero-art" role="img" aria-label="Watercolor American flag with silhouettes of saluting service members and families"></div>

  <p class="offer-line">CONTRACTORS OFFER <span class="accent">YOUR CUSTOMER</span></p>

  <div class="discount-band">
    <div class="discount-amount"><span class="value">$300</span><span class="off">OFF*</span></div>
    <div class="discount-audience">FOR ACTIVE MILITARY AND VETERANS</div>
  </div>

  <p class="credit-line">AND RECIEVE <span class="accent">$300</span> ACCOUNT CREDIT FROM HARBORLINE SUPPLY</p>
  <p class="credit-note">(Just Complete Submitted form)</p>

  <div class="order-terms">Delivered orders only with a $3,000 pretax minimum. Max 5 times per year</div>

  <p class="fine-print">Terms &amp; Conditions: This program is intended for the professional contractors that delivered Harborline Supply with material purchases. One-time purchasers and institutions are not eligible for this program. By choosing to participate, you represent to Harborline Supply that your participation is not prohibited by law. Harborline Supply reserves the right to cancel, suspend, and/or modify this promotion at any time, for any reason, without prior notice. Employees at Harborline Supply are not eligible to participate. All rights reserved by Harborline Supply. Promotion expires December 31, 2024.</p>

  <p class="social">Follow Us @harborlinesupply</p>
</main>
</body>
</html>
```